Business Card Design

Hello,
I try and keep my business card fresh and current. So about every year i get a new one. This year I'd like something with a white background and black lettering.
Before you start - I do not want my phone number or any other description on the card other than my url and my email.

I'd like a double sided business card with
TobFarnsby.com on one side

and

Tob@TobFarnsby.com on the other side of the card

Thinking very minimalistic and modern.
I don't have a particular font i mind or how to capitalize my name or website. This card will lead people to my new website that is being designed to showcase my photography and music.

* Initial thought was the front side of the card having a grid-like pattern built out of dashes or periods, with my website sitting within the pattern and on the back side my email on a stark white background. But that might look completely lame - haha.

I'm looking forward to seeing what you come up with.

thank you,
- tob farnsby

Reason: Want to spend some more time with the designs and add a little $. thanks for all the designs - tob

Wanted to add a little $ and spend some more time with the designs.

big thanks to all who have submitted work 

- tob

Industry/Entity Type

Business

Contact Information for Business Card

www.tobfarnsby.com
tob@tobfarnsby.com

Colors
000000
ffffff

Requirements
Must have
• tobfarnsby.com
tob@tobfarnsby.com
Should not have
• phone number
any description of what i do, photography or music

```html
<!DOCTYPE html>
<html lang="en">
<head>
<meta charset="utf-8">
<title>Tob Farnsby — Business Card</title>
<link href="https://fonts.googleapis.com/css2?family=Open+Sans:wght@400&display=swap" rel="stylesheet">
<style>
  :root {
    --backdrop: #d4d4d7;
    --card-dark: #0e0e0e;
    --card-dark-tone: #1e1e1e;
    --card-light: #ffffff;
    --ink-light: #ffffff;
    --ink-dark: #111111;
    --card-shadow: rgba(0, 0, 0, 0.28);
  }
  html, body {
    margin: 0;
    padding: 0;
    width: 883px;
    height: 1200px;
    overflow: hidden;
    background: var(--backdrop);
  }
  .canvas {
    position: relative;
    width: 883px;
    height: 1200px;
    display: flex;
    flex-direction: column;
    align-items: center;
    justify-content: center;
    gap: 16px;
  }
  .card {
    position: relative;
    width: 390px;
    display: flex;
    align-items: center;
    justify-content: center;
    box-shadow: 0 5px 7px -3px var(--card-shadow);
    font-family: "Open Sans", Arial, sans-serif;
    font-weight: 400;
    font-size: 21px;
    letter-spacing: 2px;
  }
  .card--front {
    height: 220px;
    color: var(--ink-light);
  }
  .card--back {
    height: 204px;
    background: var(--card-light);
    color: var(--ink-dark);
  }
  .card__pattern {
    position: absolute;
    inset: 0;
    background: linear-gradient(135deg, var(--card-dark-tone), var(--card-dark) 60%, var(--card-dark-tone));
  }
  .card__text {
    position: relative;
    margin: 0;
  }
</style>
</head>
<body>
  <main class="canvas">
    <section class="card card--front">
      <div class="card__pattern" role="img" aria-label="Fine white crosshatch grid pattern on black"></div>
      <p class="card__text card__url">www.tobfarnsby.com</p>
    </section>
    <section class="card card--back">
      <p class="card__text card__email">tob@tobfarnsby.com</p>
    </section>
  </main>
</body>
</html>
```